High performance dog care

We need a high performance care label for dog show specialists;
The relationship with the canine world can be discreet; we prefer that there are no pictures of dogs
The label will be affixed to a round bottle (see photo);
This tag measures 150mm wide by 170mm high; the visible part for the front graphics is 45mm wide by 170mm high
These products are intended for competitors in the dog grooming and breeding sectors.
The addition of foil (gold or silver) is quite possible

Target Market(s)

Professional dog shows

Industry/Entity Type

Cosmetics

Requirements
Must have
• An elegant and technical look
The word "Vell" as a title
Subtitle: for example: Argan
Description: nourishing treatment (in English and French)
In text or symbol: no para ben, no silicone, no sulfate, no dyes
Nice to have
• There are currently 4 different products which should be distinct from each other while together forming a homogeneity of the range
- nourishing treatment: argan, jojoba oil, almond oil
- volumizing treatment: keratin and hyaluronic acid
- smoothing treatment: silk protein from JApon
- restructuring treatment: avocado and macadamia oil
-
Should not have
• Humorous cartoons

```html
<!DOCTYPE html>
<html lang="en">
<head>
<meta charset="utf-8">
<title>Vell — Dog Care Range Labels</title>
<link rel="stylesheet" href="https://fonts.googleapis.com/css2?family=Space+Mono:wght@400;700&family=Lato:wght@300;400&display=swap">
<style>
  :root {
    --page: #ffffff;
    --label: #edf0ef;
    --label-edge: #e2e6e5;
    --ink: #1f2223;
    --ink-soft: #4a4f51;
    --ink-muted: #6b7072;
    --argan: #d99a3a;
    --argan-light: #e6b868;
    --keratin: #b8122f;
    --keratin-light: #d9426f;
    --silk: #2f86dc;
    --silk-light: #6db6ee;
    --avocado: #6eb42a;
    --avocado-light: #9bd052;
  }
  * { box-sizing: border-box; margin: 0; padding: 0; }
  html, body {
    width: 1200px;
    height: 898px;
    overflow: hidden;
    background: var(--page);
  }
  .range {
    position: relative;
    width: 1200px;
    height: 898px;
  }
  .label {
    position: absolute;
    top: 226px;
    width: 168px;
    height: 628px;
    background: var(--label);
    border: 1px solid var(--label-edge);
    border-radius: 14px;
  }
  .label--argan   { left: 98px;  --accent: var(--argan);   --accent-light: var(--argan-light); }
  .label--keratin { left: 359px; --accent: var(--keratin); --accent-light: var(--keratin-light); }
  .label--silk    { left: 636px; --accent: var(--silk);    --accent-light: var(--silk-light); }
  .label--avocado { left: 922px; --accent: var(--avocado); --accent-light: var(--avocado-light); }

  .brand {
    position: absolute;
    top: 118px;
    left: 14px;
    display: flex;
    align-items: center;
    gap: 10px;
    font-family: "Lato", sans-serif;
    font-weight: 300;
    font-size: 46px;
    line-height: 1;
    letter-spacing: 2px;
    text-transform: uppercase;
    color: var(--ink);
  }
  .brand-mark {
    width: 10px;
    height: 10px;
    background: var(--ink);
  }
  .variant-tab {
    position: absolute;
    top: 234px;
    left: -1px;
    height: 33px;
    padding: 0 8px 0 12px;
    display: flex;
    align-items: center;
    background: linear-gradient(90deg, var(--accent), var(--accent-light) 55%, var(--accent));
    font-family: "Lato", sans-serif;
    font-weight: 300;
    font-size: 19px;
    letter-spacing: 0.3px;
    color: #ffffff;
  }
  .benefit {
    position: absolute;
    left: 12px;
    right: 4px;
  }
  .benefit--en { top: 358px; }
  .benefit--fr { top: 409px; }
  .benefit-title {
    font-family: "Space Mono", monospace;
    font-weight: 400;
    font-size: 16px;
    line-height: 1.15;
    letter-spacing: -0.5px;
    color: var(--accent);
  }
  .benefit-ingredients {
    font-family: "Lato", sans-serif;
    font-weight: 300;
    font-size: 11px;
    line-height: 1.3;
    color: var(--ink-soft);
  }
  .free-from {
    position: absolute;
    top: 518px;
    left: 14px;
    list-style: none;
    font-family: "Lato", sans-serif;
    font-weight: 300;
    font-size: 11.5px;
    line-height: 14.6px;
    color: var(--ink-muted);
  }
  .free-from li {
    display: flex;
    align-items: center;
    gap: 5px;
  }
  .tick { width: 7px; height: 9px; flex: none; }
  .volume {
    position: absolute;
    bottom: 10px;
    left: 0;
    right: 0;
    text-align: center;
    font-family: "Space Mono", monospace;
    font-weight: 700;
    font-size: 12px;
    color: var(--ink);
  }
</style>
</head>
<body>
<main class="range">

  <section class="label label--argan">
    <div class="brand">Vell<span class="brand-mark"></span></div>
    <div class="variant-tab">ARGAN</div>
    <div class="benefit benefit--en">
      <h2 class="benefit-title">Nourishing</h2>
      <p class="benefit-ingredients">Argan, jojoba oil, almond oil</p>
    </div>
    <div class="benefit benefit--fr" lang="fr">
      <h2 class="benefit-title">Nourrissant</h2>
      <p class="benefit-ingredients">Arganier, huile de jojoba,<br>huile d'amande</p>
    </div>
    <ul class="free-from">
      <li><svg class="tick" viewBox="0 0 7 9"><polyline points="0.5,5.5 2,8.5 6.5,0.5" fill="none" stroke="currentColor" stroke-width="0.9"/></svg>paraben free</li>
      <li><svg class="tick" viewBox="0 0 7 9"><polyline points="0.5,5.5 2,8.5 6.5,0.5" fill="none" stroke="currentColor" stroke-width="0.9"/></svg>silicone free</li>
      <li><svg class="tick" viewBox="0 0 7 9"><polyline points="0.5,5.5 2,8.5 6.5,0.5" fill="none" stroke="currentColor" stroke-width="0.9"/></svg>sulfate free</li>
      <li><svg class="tick" viewBox="0 0 7 9"><polyline points="0.5,5.5 2,8.5 6.5,0.5" fill="none" stroke="currentColor" stroke-width="0.9"/></svg>dyes free</li>
    </ul>
    <p class="volume">500 ml</p>
  </section>

  <section class="label label--keratin">
    <div class="brand">Vell<span class="brand-mark"></span></div>
    <div class="variant-tab">KERATIN</div>
    <div class="benefit benefit--en">
      <h2 class="benefit-title">Volumizing</h2>
      <p class="benefit-ingredients">Keratin and hyaluronic acid</p>
    </div>
    <div class="benefit benefit--fr" lang="fr">
      <h2 class="benefit-title">Volumisant</h2>
      <p class="benefit-ingredients">Kératine et acide hyaluronique</p>
    </div>
    <ul class="free-from">
      <li><svg class="tick" viewBox="0 0 7 9"><polyline points="0.5,5.5 2,8.5 6.5,0.5" fill="none" stroke="currentColor" stroke-width="0.9"/></svg>paraben free</li>
      <li><svg class="tick" viewBox="0 0 7 9"><polyline points="0.5,5.5 2,8.5 6.5,0.5" fill="none" stroke="currentColor" stroke-width="0.9"/></svg>silicone free</li>
      <li><svg class="tick" viewBox="0 0 7 9"><polyline points="0.5,5.5 2,8.5 6.5,0.5" fill="none" stroke="currentColor" stroke-width="0.9"/></svg>sulfate free</li>
      <li><svg class="tick" viewBox="0 0 7 9"><polyline points="0.5,5.5 2,8.5 6.5,0.5" fill="none" stroke="currentColor" stroke-width="0.9"/></svg>dyes free</li>
    </ul>
    <p class="volume">500 ml</p>
  </section>

  <section class="label label--silk">
    <div class="brand">Vell<span class="brand-mark"></span></div>
    <div class="variant-tab">SILK</div>
    <div class="benefit benefit--en">
      <h2 class="benefit-title">Smoothing</h2>
      <p class="benefit-ingredients">Silk protein from Japan</p>
    </div>
    <div class="benefit benefit--fr" lang="fr">
      <h2 class="benefit-title">Lissage</h2>
      <p class="benefit-ingredients">Protéine de soie du Japon</p>
    </div>
    <ul class="free-from">
      <li><svg class="tick" viewBox="0 0 7 9"><polyline points="0.5,5.5 2,8.5 6.5,0.5" fill="none" stroke="currentColor" stroke-width="0.9"/></svg>paraben free</li>
      <li><svg class="tick" viewBox="0 0 7 9"><polyline points="0.5,5.5 2,8.5 6.5,0.5" fill="none" stroke="currentColor" stroke-width="0.9"/></svg>silicone free</li>
      <li><svg class="tick" viewBox="0 0 7 9"><polyline points="0.5,5.5 2,8.5 6.5,0.5" fill="none" stroke="currentColor" stroke-width="0.9"/></svg>sulfate free</li>
      <li><svg class="tick" viewBox="0 0 7 9"><polyline points="0.5,5.5 2,8.5 6.5,0.5" fill="none" stroke="currentColor" stroke-width="0.9"/></svg>dyes free</li>
    </ul>
    <p class="volume">500 ml</p>
  </section>

  <section class="label label--avocado">
    <div class="brand">Vell<span class="brand-mark"></span></div>
    <div class="variant-tab">AVOCADO</div>
    <div class="benefit benefit--en">
      <h2 class="benefit-title">Restructuring</h2>
      <p class="benefit-ingredients">Avocado and macadamia</p>
    </div>
    <div class="benefit benefit--fr" lang="fr">
      <h2 class="benefit-title">Restructuration</h2>
      <p class="benefit-ingredients">Avocat et macadamia</p>
    </div>
    <ul class="free-from">
      <li><svg class="tick" viewBox="0 0 7 9"><polyline points="0.5,5.5 2,8.5 6.5,0.5" fill="none" stroke="currentColor" stroke-width="0.9"/></svg>paraben free</li>
      <li><svg class="tick" viewBox="0 0 7 9"><polyline points="0.5,5.5 2,8.5 6.5,0.5" fill="none" stroke="currentColor" stroke-width="0.9"/></svg>silicone free</li>
      <li><svg class="tick" viewBox="0 0 7 9"><polyline points="0.5,5.5 2,8.5 6.5,0.5" fill="none" stroke="currentColor" stroke-width="0.9"/></svg>sulfate free</li>
      <li><svg class="tick" viewBox="0 0 7 9"><polyline points="0.5,5.5 2,8.5 6.5,0.5" fill="none" stroke="currentColor" stroke-width="0.9"/></svg>dyes free</li>
    </ul>
    <p class="volume">500 ml</p>
  </section>

</main>
</body>
</html>
```